Business card for a new cabinet shop company named Torvane Cabinets for high end cabinets

Design a business card, thinking dark rich green with colours to speak of high end luxury ie; cream, gold, black possibly

Miles Harwick
Director Craftsman
Email: info@torvanecabinets.com.au
Instagram : @torvane.cabinets

```html
<!DOCTYPE html>
<html lang="en">
<head>
<meta charset="utf-8">
<title>Torvane Cabinets – Business Card</title>
<link rel="stylesheet" href="https://fonts.googleapis.com/css2?family=Montserrat:wght@400;700&display=swap">
<style>
  :root {
    --backdrop: #9a9a9a;
    --card: #14291f;
    --gold: #c5a466;
    --cream: #f1ece0;
    --silver: #d8d4c8;
  }
  * { margin: 0; padding: 0; box-sizing: border-box; }
  html, body { width: 1200px; height: 1108px; overflow: hidden; }
  body {
    background: var(--backdrop);
    font-family: "Montserrat", sans-serif;
    position: relative;
  }
  .card {
    position: absolute;
    left: 242px;
    width: 715px;
    height: 409px;
    border-radius: 30px;
    background: var(--card);
  }
  .card--front { top: 119px; }
  .card--back { top: 580px; }

  .front-name {
    position: absolute;
    inset: 0;
    display: flex;
    align-items: center;
    justify-content: center;
    color: var(--silver);
    font-size: 46px;
    font-weight: 400;
    letter-spacing: 1px;
  }

  .back-brand {
    position: absolute;
    left: 43px;
    top: 186px;
    width: 300px;
    color: var(--gold);
    font-size: 28px;
    font-weight: 400;
    white-space: nowrap;
  }
  .divider {
    position: absolute;
    left: 356px;
    top: 82px;
    width: 2px;
    height: 247px;
    background: var(--gold);
  }
  .details {
    position: absolute;
    left: 380px;
    top: 78px;
    color: var(--cream);
  }
  .details__name {
    color: var(--gold);
    font-size: 30px;
    font-weight: 700;
    line-height: 1.2;
  }
  .details__title {
    font-size: 18px;
    line-height: 1.2;
    margin-top: 4px;
  }
  .details__address {
    font-size: 18px;
    line-height: 28px;
    margin-top: 18px;
  }
  .contact-list { list-style: none; margin-top: 12px; }
  .contact-list li {
    display: flex;
    align-items: center;
    font-size: 18.5px;
    height: 28.5px;
  }
  .contact-list svg {
    width: 16px;
    height: 16px;
    margin-right: 8px;
    flex: none;
    fill: var(--gold);
  }
  .contact-list .icon-cut { fill: none; stroke: var(--card); }
  .contact-list .icon-ring { fill: none; stroke: var(--gold); stroke-width: 1.6; }
</style>
</head>
<body>
  <section class="card card--front">
    <div class="front-name">Torvane Cabinets</div>
  </section>

  <section class="card card--back">
    <div class="back-brand">Torvane Cabinets</div>
    <div class="divider"></div>
    <div class="details">
      <div class="details__name">Miles Harwick</div>
      <div class="details__title">Director Craftsman</div>
      <div class="details__address">Your address, City<br>State, Zip 1234</div>
      <ul class="contact-list">
        <li>
          <svg viewBox="0 0 16 16"><path d="M1 6c0-2 3-3 7-3s7 1 7 3v1h-3V5.5H4V7H1z"/><rect x="3" y="8" width="10" height="5" rx="1"/></svg>
          123 456 789
        </li>
        <li>
          <svg viewBox="0 0 16 16"><path d="M1 3h14v10H1z"/><path class="icon-cut" d="M1.5 3.5 8 9l6.5-5.5" stroke-width="1.3"/></svg>
          info@torvanecabinets.com.au
        </li>
        <li>
          <svg viewBox="0 0 16 16"><circle class="icon-ring" cx="8" cy="8" r="6.5"/></svg>
          @torvane.cabinets
        </li>
        <li>
          <svg viewBox="0 0 16 16"><circle cx="8" cy="8" r="7"/><path class="icon-cut" d="M1 8h14M8 1c-3 3-3 11 0 14M8 1c3 3 3 11 0 14" stroke-width="1"/></svg>
          www.torvanecabinets.com.au
        </li>
      </ul>
    </div>
  </section>
</body>
</html>
```